New Facebook Banner

Hi
We are operating Ramen shop in Australia.(http://mizunokobowls.com)
I want to create new design for our Facebook banner and title is "Free Ramen on your Birthday".
Sample attached is our existing banner design. We would like to make it more modern and sophisticated.
We are so looking forward to seeing your design for our free ramen promotion.

https://www.facebook.com/mizunokobowls/

Industry/Entity Type

Japanese Restaurant

Font styles to use
Sans Serif

```html
<!DOCTYPE html>
<html lang="en">
<head>
<meta charset="utf-8">
<title>Free Ramen on Your Birthday – Mizunoko Bowls</title>
<link href="https://fonts.googleapis.com/css2?family=Open+Sans:wght@400;700;800&display=swap" rel="stylesheet">
<style>
  :root {
    --ink: #111111;
    --tag-light: #ffd21a;
    --tag-dark: #f79a00;
    --tag-edge: #f3b400;
    --dash: #ffffff;
    --splash-core: #ff9a12;
    --splash-edge: #ffc21a;
    --wash-pink: #f25fc0;
    --wash-cyan: #3fd0ea;
    --wash-yellow: #ffe45a;
    --wash-orange: #ff8a3c;
    --wash-red: #ff5a3a;
    --wash-light: #f4f1ee;
  }
  html, body {
    margin: 0;
    padding: 0;
    overflow: hidden;
    background: #ffffff;
  }
  .banner {
    position: relative;
    width: 1200px;
    height: 444px;
    overflow: hidden;
    font-family: "Open Sans", Arial, sans-serif;
    color: var(--ink);
  }
  .party-backdrop {
    position: absolute;
    inset: 0;
    background:
      radial-gradient(ellipse 260px 200px at 240px 30px, var(--wash-pink), transparent 70%),
      radial-gradient(ellipse 220px 260px at 40px 400px, var(--wash-pink), transparent 70%),
      radial-gradient(ellipse 280px 220px at 560px 330px, var(--wash-cyan), transparent 72%),
      radial-gradient(ellipse 240px 200px at 930px 120px, var(--wash-yellow), transparent 72%),
      radial-gradient(ellipse 260px 260px at 1150px 220px, var(--wash-red), transparent 70%),
      radial-gradient(ellipse 300px 200px at 880px 420px, var(--wash-orange), transparent 72%),
      var(--wash-light);
  }
  .brush-splash {
    position: absolute;
    left: 625px;
    top: 135px;
    width: 350px;
    height: 200px;
    border-radius: 46% 54% 40% 60% / 55% 45% 55% 45%;
    background: radial-gradient(ellipse at 50% 50%, var(--splash-core) 55%, var(--splash-edge) 80%, transparent 100%);
  }
  .brand-tag {
    position: absolute;
    left: 48px;
    top: 62px;
    width: 272px;
    height: 272px;
  }
  .brand-name {
    position: absolute;
    left: 80px;
    top: 172px;
    width: 200px;
    display: flex;
    align-items: center;
    gap: 10px;
    font-size: 26px;
    font-weight: 800;
    line-height: 1.05;
    color: var(--ink);
  }
  .brand-dot {
    flex: none;
    width: 22px;
    height: 22px;
    border-radius: 50%;
    background: var(--ink);
  }
  .offer {
    position: absolute;
    left: 650px;
    top: 150px;
    width: 300px;
    text-align: center;
    line-height: 1;
  }
  .offer-free {
    display: block;
    font-size: 41px;
    font-weight: 800;
    letter-spacing: 0.5px;
  }
  .offer-item {
    display: block;
    margin-top: 6px;
    font-size: 52px;
    font-weight: 400;
  }
  .offer-on {
    display: block;
    margin-top: 8px;
    font-size: 20px;
    font-weight: 400;
  }
  .offer-occasion {
    display: block;
    margin-top: 10px;
    font-size: 22px;
    font-weight: 800;
    letter-spacing: 1px;
  }
</style>
</head>
<body>
  <main class="banner">
    <div class="party-backdrop" role="img" aria-label="Colourful watercolour party backdrop with balloons, bunting flags, gift boxes, party hats and confetti"></div>
    <div class="brush-splash" role="img" aria-label="Orange paint brush splash behind the offer text"></div>

    <svg class="brand-tag" viewBox="0 0 272 272" aria-hidden="true">
      <defs>
        <linearGradient id="tagFill" x1="0" y1="0" x2="1" y2="0">
          <stop offset="0" stop-color="var(--tag-light)"/>
          <stop offset="1" stop-color="var(--tag-dark)"/>
        </linearGradient>
      </defs>
      <polygon points="0,0 220,0 272,136 220,272 0,272" fill="url(#tagFill)" stroke="var(--tag-edge)" stroke-width="2"/>
      <polygon points="8,9 213,9 262,136 213,263 8,263" fill="none" stroke="var(--dash)" stroke-width="2" stroke-dasharray="5 4"/>
    </svg>
    <div class="brand-name">
      <span class="brand-dot"></span>
      <span>Mizunoko Bowls</span>
    </div>

    <h1 class="offer" style="margin:0;font-weight:400;">
      <span class="offer-free">FREE</span>
      <span class="offer-item">RAMEN</span>
      <span class="offer-on">ON</span>
      <span class="offer-occasion">YOUR BIRTHDAY</span>
    </h1>
  </main>
</body>
</html>
```